Butcher shop

We have 2 butcher shops:

Shop 9, Ridgeway Court, Wattleford NSW 2391
Ph 02 6512 3840

47 Marlow St, Kurrabin NSW 2394
Ph 02 6518 2274

ABN 48 907 215 816

I would like this info on reverse of card and my personal info on front of card. I have a logo I would like to use also. Require a very smooth thick matte card, with colour both sides.

Front of card should say:

Linda Farrugia
Accounts

Ph 0437 620 915
E lindafarrugia@quollmail.com.au

Industry/Entity Type

Shop

Contact Information for Business Card

Linda Farrugia
Ph 0437 620 915

Logo Text

Farrugia's Quality Meats

Logo styles of interest
Pictorial/Combination Logo
Requirements
Must have
• We use Century Gothic Font

```html
<!DOCTYPE html>
<html lang="en">
<head>
<meta charset="utf-8">
<title>Farrugia's Quality Meats – Business Card</title>
<link rel="stylesheet" href="https://fonts.googleapis.com/css2?family=Questrial&family=Mulish:wght@700&display=swap">
<style>
  :root {
    --page-bg: #ececec;
    --card-bg: #ffffff;
    --brand-blue: #80e1fc;
    --ink: #333333;
    --rule: #263844;
    --edge: #d4d4d4;
  }
  * { box-sizing: border-box; margin: 0; padding: 0; }
  html, body {
    width: 997px; height: 1200px; overflow: hidden;
    background: var(--page-bg);
  }
  body { position: relative; font-family: "Questrial", "Century Gothic", sans-serif; color: var(--ink); }

  .card {
    position: absolute;
    background: var(--card-bg);
    border: 1px solid var(--edge);
    overflow: hidden;
  }
  .card--front { left: 78px; top: 103px; width: 819px; height: 455px; }
  .card--back  { left: 88px; top: 674px; width: 820px; height: 457px; }

  .brand-panel {
    position: absolute; left: 0; top: 0; bottom: 0;
    background: var(--brand-blue);
  }
  .card--front .brand-panel { width: 268px; }
  .card--back .brand-panel { width: 266px; }

  .brand-mark {
    position: absolute; left: 50%; width: 44px; height: 44px;
    margin-left: -22px; border-radius: 50%;
    background: var(--ink);
  }
  .card--front .brand-mark { top: 209px; }
  .card--back .brand-mark { top: 209px; }

  .brand-name {
    position: absolute; left: 0; right: 0;
    text-align: center;
    font-size: 26px; line-height: 31px;
    color: var(--ink);
  }
  .card--front .brand-name { top: 260px; }
  .card--back .brand-name { top: 263px; }

  .divider {
    position: absolute; width: 3px; background: var(--rule);
  }
  .card--front .divider { left: 265px; top: 151px; height: 204px; }
  .card--back .divider { left: 263px; top: 152px; height: 202px; }

  .person { position: absolute; left: 377px; top: 112px; }
  .person__name {
    font-family: "Mulish", "Century Gothic", sans-serif;
    font-weight: 700; font-size: 32px; line-height: 38px;
  }
  .person__role { font-size: 34px; line-height: 40px; }

  .contact-line {
    position: absolute; display: flex; align-items: center;
    font-size: 26px; line-height: 30px; white-space: nowrap;
  }
  .contact-line svg { position: absolute; fill: var(--ink); }
  .card--front .contact-line { left: 377px; }
  .card--front .contact-line svg { left: -27px; width: 16px; height: 16px; }
  .contact-line--phone { top: 274px; }
  .contact-line--email { top: 313px; }

  .shop-info { position: absolute; left: 323px; font-size: 22px; line-height: 32px; white-space: nowrap; }
  .shop-info__phone { position: relative; font-weight: 700; font-family: "Mulish", "Century Gothic", sans-serif; font-size: 22px; }
  .shop-info__phone svg { position: absolute; left: -20px; top: 8px; width: 15px; height: 16px; fill: var(--ink); }
  .shop-info--first { top: 144px; }
  .shop-info--second { top: 239px; }
  .shop-info--abn { top: 333px; }
</style>
</head>
<body>

<section class="card card--front" aria-label="Business card front">
  <div class="brand-panel">
    <span class="brand-mark" aria-hidden="true"></span>
    <p class="brand-name">Farrugia's<br>Quality Meats</p>
  </div>
  <div class="divider"></div>
  <div class="person">
    <p class="person__name">Linda Farrugia</p>
    <p class="person__role">Accounts</p>
  </div>
  <p class="contact-line contact-line--phone">
    <svg viewBox="0 0 16 16" aria-hidden="true"><path d="M4.2 1.2 6 4.3 4.6 5.6c.7 2.4 2.6 4.6 4.9 5.8l1.4-1.3 3 2L12.6 14.6C7.3 14.5 1.6 8.6 1.6 3.2z"/></svg>
    0437 620 915
  </p>
  <p class="contact-line contact-line--email">
    <svg viewBox="0 0 16 16" aria-hidden="true"><path d="M1 4h14v9H1z"/><path d="M1 4l7 5 7-5" fill="none" stroke="#fff" stroke-width="1.4"/></svg>
    lindafarrugia@quollmail.com.au
  </p>
</section>

<section class="card card--back" aria-label="Business card back">
  <div class="brand-panel">
    <span class="brand-mark" aria-hidden="true"></span>
    <p class="brand-name">Farrugia's<br>Quality Meats</p>
  </div>
  <div class="divider"></div>
  <div class="shop-info shop-info--first">
    <p>Shop 9, Ridgeway Court, Wattleford NSW 2391</p>
    <p class="shop-info__phone"><svg viewBox="0 0 16 16" aria-hidden="true"><path d="M4.2 1.2 6 4.3 4.6 5.6c.7 2.4 2.6 4.6 4.9 5.8l1.4-1.3 3 2L12.6 14.6C7.3 14.5 1.6 8.6 1.6 3.2z"/></svg>02 6512 3840</p>
  </div>
  <div class="shop-info shop-info--second">
    <p>47 Marlow St, Kurrabin NSW 2394</p>
    <p class="shop-info__phone"><svg viewBox="0 0 16 16" aria-hidden="true"><path d="M4.2 1.2 6 4.3 4.6 5.6c.7 2.4 2.6 4.6 4.9 5.8l1.4-1.3 3 2L12.6 14.6C7.3 14.5 1.6 8.6 1.6 3.2z"/></svg>02 6518 2274</p>
  </div>
  <p class="shop-info shop-info--abn">ABN 48 907 215 816</p>
</section>

</body>
</html>
```